Create a Graphic About YOURSELF and PixelHarbor

PixelHarbor would like you (designers) to create an awesome graphic to promote YOURSELF and your profile on PixelHarbor!

Your graphic should communicate your name, your services and should mention PixelHarbor.

The design should be perfect for sharing on Chatterly. Here's an example of what we'd like http://blog.pixelharbor-example.ca/article/333/pixelharbor-launches-3000-hire-me-social-design-contest

Once you submitted your design, we'd love you to share the design ('advertisement') and promote yourself and PixelHarbor to your friends and potential customers. So make your submissions great and get your friends to vote for your design by 'Liking' it on Chatterly!

Prizes:
$1500 - "PixelHarbor Community" prize awarded to the designer with the most Chatterly 'Likes'
5 x $50 for the next 5 'most liked' designs on Chatterly

$1000 - "Hire Me" prize awarded to the designer who receives the most client invites
5 x $50 for the next 5 'most invited' designers

In summary, this is a great opportunity for you to increase your exposure to PixelHarbor customers and win cash prizes. Show off your design skills and get hired by PixelHarbor customers from around the world!

Target Market(s)

Fans, friends and customers of YOU

Industry/Entity Type

Cash

Requirements
Must have
• 1) Include your PixelHarbor user name on the graphic so customers can find you in the PixelHarbor Designer Directory
2) Include the tagline "Hire Me on PixelHarbor.com!" in your graphic design.
3) Share your design's URL on our Chatterly wall at http://chatterly-example.com/pixelharbor and get your friends to 'like' your design.
Nice to have
• 1) Include a tagline that expresses your design approach/philosophy
2) Artwork dimensions: 403 x 403 px
3) You can submit more than 1 design!
Should not have
• You must own the copyright of any images you use including stock imagery.

```html
<!DOCTYPE html>
<html lang="en">
<head>
<meta charset="utf-8">
<title>One Word: Mind-Blowing — Kayveem on PixelHarbor</title>
<link rel="stylesheet" href="https://fonts.googleapis.com/css2?family=Anton&family=Oswald:wght@700&display=swap">
<style>
  :root {
    --paper: #ffffff;
    --ink: #111111;
    --accent-magenta: #ff1fa8;
    --band-yellow: #ffe600;
    --band-lime: #c8e81a;
    --art-pink: #f23a9c;
    --art-lime: #b9f23a;
    --art-sky: #3ab8f2;
    --art-violet: #8c5ad8;
  }
  * { margin: 0; padding: 0; box-sizing: border-box; }
  html, body { width: 1200px; height: 1200px; overflow: hidden; background: var(--paper); }
  .poster {
    position: relative;
    width: 1200px;
    height: 1200px;
    overflow: hidden;
    background: var(--paper);
  }
  .poster__shapes {
    position: absolute;
    inset: 0;
    width: 1200px;
    height: 1200px;
  }
  .message {
    position: absolute;
    left: 563px;
    top: 975px;
    color: var(--ink);
  }
  .message__headline {
    font-family: "Anton", "Impact", sans-serif;
    font-size: 70px;
    line-height: 0.92;
    letter-spacing: 1px;
    text-transform: uppercase;
    font-weight: 400;
  }
  .message__pitch {
    margin-top: 14px;
    font-family: "Oswald", "Arial Narrow", sans-serif;
    font-weight: 700;
    font-size: 27px;
    line-height: 1.3;
    text-transform: uppercase;
    white-space: nowrap;
    letter-spacing: 0.2px;
  }
  .message__username { color: var(--accent-magenta); }
</style>
</head>
<body>
  <main class="poster">
    <svg class="poster__shapes" viewBox="0 0 1200 1200" aria-hidden="false">
      <defs>
        <linearGradient id="bandGradient" x1="0" y1="0" x2="0" y2="1">
          <stop offset="0" stop-color="var(--band-lime)"/>
          <stop offset="0.35" stop-color="var(--band-yellow)"/>
          <stop offset="1" stop-color="var(--band-yellow)"/>
        </linearGradient>
        <linearGradient id="cornerGradient" x1="0" y1="0" x2="1" y2="1">
          <stop offset="0" stop-color="var(--band-yellow)"/>
          <stop offset="0.6" stop-color="var(--band-lime)"/>
          <stop offset="1" stop-color="var(--art-sky)"/>
        </linearGradient>
        <radialGradient id="artGradient" cx="0.45" cy="0.35" r="0.75">
          <stop offset="0" stop-color="var(--art-pink)"/>
          <stop offset="0.3" stop-color="var(--art-violet)" stop-opacity="0.85"/>
          <stop offset="0.5" stop-color="var(--art-lime)" stop-opacity="0.7"/>
          <stop offset="0.72" stop-color="var(--art-sky)" stop-opacity="0.45"/>
          <stop offset="1" stop-color="#ffffff" stop-opacity="0"/>
        </radialGradient>
      </defs>

      <path class="side-band" d="M0,0 L170,0 Q150,620 280,1200 L0,1200 Z" fill="url(#bandGradient)"/>

      <path class="corner-strip" d="M770,0 L1200,0 L1200,450 Z" fill="url(#cornerGradient)"/>

      <path class="feature-art" role="img"
            aria-label="Collage artwork: open red lips beneath an explosion of pink, lime and blue paint scribbles, with a beaded necklace below"
            d="M188,0 L715,0 L1200,500 L1200,940 L560,940 L560,1200 L300,1200 Q170,620 188,0 Z"
            fill="url(#artGradient)"/>
    </svg>

    <section class="message">
      <h1 class="message__headline">One word:<br>Mind-blowing.</h1>
      <p class="message__pitch">Experience amazing for the first time with<br><span class="message__username">Kayveem</span>. Hire me on www.PixelHarbor.com</p>
    </section>
  </main>
</body>
</html>
```